We need a very creative business card for a leading diamond tools manufactures in india

1. Iso 9001:2000
2. Logo
3. Leading Manufacture of stone cutting tools: Gang Saw Segment, Circular Segment, wire saw segment and rubber and plastic coated diamond wire rope.
4. Spirit for success
5. Kalpa Venor Diamond Tools Pvt. Ltd.
6. Mo. No. 9846073358
7. Email: Ravik@kvtgroup-asia.com
8. Web: kvtgroup-asia.com
9.CEO
10. Reg. Office. 47, gopal vihar , purani basti, devgarh ,dist. Bhimpura (rajasthan) 305718
11.Ravik Jhalani
Target Market(s)
Our audience are Adult based in english speaking person having age between 25-55 that handle granite and marble business.
Industry/Entity Type
Plastic
Font styles to use

```html
<!DOCTYPE html>
<html lang="en">
<head>
<meta charset="utf-8">
<title>Kalpa Venor – Business Card</title>
<link rel="stylesheet" href="https://fonts.googleapis.com/css2?family=Open+Sans:wght@400;600;700&display=swap">
<style>
  :root {
    --brand-red: #a8262a;
    --brand-orange: #f0a21e;
    --ink-grey: #4a4a4a;
    --soft-grey: #6b6b6b;
    --card-white: #ffffff;
    --backdrop: #ebe8e4;
  }
  * { box-sizing: border-box; margin: 0; padding: 0; }
  html, body {
    width: 1200px;
    height: 900px;
    overflow: hidden;
    background: var(--backdrop);
    font-family: "Open Sans", Arial, sans-serif;
  }
  .canvas { position: relative; width: 1200px; height: 900px; }

  .card {
    position: absolute;
    width: 580px;
    height: 331px;
    box-shadow: 0 6px 18px rgba(0,0,0,0.18);
    overflow: hidden;
  }

  /* Reverse side */
  .card--back {
    left: 100px;
    top: 80px;
    background: var(--brand-red);
    display: flex;
    align-items: center;
    justify-content: center;
  }
  .brand-mark {
    display: flex;
    align-items: center;
    gap: 18px;
  }
  .brand-mark__dot {
    width: 46px;
    height: 46px;
    border-radius: 50%;
    border: 8px solid currentColor;
  }
  .brand-mark__name {
    font-weight: 700;
    letter-spacing: 0.5px;
  }
  .card--back .brand-mark { color: var(--card-white); }
  .card--back .brand-mark__name { font-size: 44px; }

  /* Front side */
  .card--front {
    left: 520px;
    top: 470px;
    background: var(--card-white);
  }
  .card--front .brand-mark {
    position: absolute;
    left: 38px;
    top: 128px;
    gap: 10px;
  }
  .card--front .brand-mark__dot {
    width: 30px;
    height: 30px;
    border: 5px solid var(--brand-orange);
  }
  .card--front .brand-mark__name {
    font-size: 25px;
    color: var(--brand-red);
  }

  .person {
    position: absolute;
    left: 318px;
    top: 48px;
  }
  .person__name {
    font-size: 24px;
    font-weight: 700;
    color: var(--brand-red);
    line-height: 1.1;
  }
  .person__title {
    font-size: 12px;
    color: var(--soft-grey);
    margin-top: 2px;
  }

  .address {
    position: absolute;
    left: 318px;
    top: 132px;
    width: 230px;
    font-size: 15px;
    line-height: 1.35;
    color: var(--ink-grey);
  }

  .contact-list {
    position: absolute;
    left: 318px;
    top: 210px;
    list-style: none;
  }
  .contact-list__item {
    display: flex;
    align-items: center;
    gap: 10px;
    font-size: 16px;
    color: var(--ink-grey);
    height: 27px;
  }
  .contact-list__icon { width: 13px; height: 13px; fill: var(--brand-orange); flex: none; }

  .footer-band {
    position: absolute;
    left: 0;
    bottom: 0;
    width: 580px;
    height: 34px;
  }
</style>
</head>
<body>
<main class="canvas">

  <section class="card card--back" aria-label="Card reverse">
    <div class="brand-mark">
      <span class="brand-mark__dot"></span>
      <span class="brand-mark__name">Kalpa Venor</span>
    </div>
  </section>

  <section class="card card--front" aria-label="Card front">
    <div class="brand-mark">
      <span class="brand-mark__dot"></span>
      <span class="brand-mark__name">Kalpa Venor</span>
    </div>

    <div class="person">
      <h1 class="person__name">Marek Delano</h1>
      <p class="person__title">Director</p>
    </div>

    <p class="address">Suite 4C, Level 3 615 Harbour Road Lindale NSW 2190</p>

    <ul class="contact-list">
      <li class="contact-list__item">
        <svg class="contact-list__icon" viewBox="0 0 24 24" aria-hidden="true"><path d="M6.6 10.8a15.1 15.1 0 0 0 6.6 6.6l2.2-2.2a1 1 0 0 1 1-.25 11.4 11.4 0 0 0 3.6.57 1 1 0 0 1 1 1V20a1 1 0 0 1-1 1A17 17 0 0 1 3 4a1 1 0 0 1 1-1h3.5a1 1 0 0 1 1 1c0 1.25.2 2.45.57 3.57a1 1 0 0 1-.25 1z"/></svg>
        <span>0498 312 547</span>
      </li>
      <li class="contact-list__item">
        <svg class="contact-list__icon" viewBox="0 0 24 24" aria-hidden="true"><path d="M2 5h20v14H2z" /><path d="M2 5l10 8 10-8" fill="none" stroke="#fff" stroke-width="2"/></svg>
        <span>hello@sitemail.com</span>
      </li>
      <li class="contact-list__item">
        <svg class="contact-list__icon" viewBox="0 0 24 24" aria-hidden="true"><circle cx="12" cy="12" r="10"/><path d="M2 12h20M12 2c3 3 3 17 0 20M12 2c-3 3-3 17 0 20" fill="none" stroke="#fff" stroke-width="1.6"/></svg>
        <span>www.sitemail.com</span>
      </li>
    </ul>

    <svg class="footer-band" viewBox="0 0 580 34" aria-hidden="true">
      <polygon points="0,20 340,20 348,34 0,34" fill="var(--brand-orange)"/>
      <polygon points="356,20 580,20 580,34 364,34" fill="var(--brand-red)"/>
      <polygon points="356,20 580,8 580,20" fill="var(--brand-red)"/>
    </svg>
  </section>

</main>
</body>
</html>
```